Redesign This Psychology Website

We would like a slight redesign of this successful psychology (relationship counselling) website:

www.TheLumaHaven.com.au

We are updating the website, and we'd like a slight refresh of the design and style.

Please keep to very similar colours, and use the same logo. We're looking for around 10 page templates, however the main one is the home page.

Keep in mind, this website already converts quite well, so we want a new, fresh design in keeping with this one. Please don't bother designing something too extremely different.

thanks :)
Updates

Target Market(s)

couples who are looking for relationship counselling. Men and women, 25 - 70, across Australia

Industry/Entity Type

Psychology

Number of Pages Required

5+ page

Font styles to use
Sans Serif

Colors
87cfc6
b7a5cd
ec1f27
ffffff
cee9f5

Requirements
Must have
• a similar look to the current design, just looking for a slight refresh.
• Search bar
• Areas for lots of photos
• same logo
• lots of content areas
Nice to have
• great content areas, where we can display a lot of content and our areas.
Should not have
• no colors like orange, etc.
• should not have a totally different feel.

```html
<!DOCTYPE html>
<html lang="en">
<head>
<meta charset="utf-8">
<title>The Luma Haven – Relationship Counselling</title>
<link href="https://fonts.googleapis.com/css2?family=Montserrat:wght@400;600;700&family=Open+Sans:wght@400;600;700&display=swap" rel="stylesheet">
<style>
:root{
  --teal:#2a8a90;
  --teal-dark:#1c6a70;
  --teal-light:#87cfc6;
  --green:#8cc63f;
  --red:#e3242b;
  --ink:#333a3d;
  --muted:#6d7578;
  --line:#dfe3e4;
  --page:#f1f2f2;
  --white:#ffffff;
  --sky:#cee9f5;
  --lilac:#b7a5cd;
  --navy:#22313a;
}
*{box-sizing:border-box;margin:0;padding:0}
html,body{width:1200px;height:4545px;overflow:hidden}
body{background:var(--page);font-family:"Open Sans",Arial,sans-serif;color:var(--ink);font-size:12.5px;line-height:1.55}
a{color:inherit;text-decoration:none}
.photo{display:block;border-radius:2px}
.wrap{width:900px;margin:0 auto;position:relative}

/* top bar */
.topbar{height:36px;background:var(--teal-dark);color:#d9eeee;font-size:11.5px}
.topbar .wrap{display:flex;justify-content:space-between;align-items:center;height:36px}
.topbar span{margin:0 6px}
/* header */
.header{height:94px;background:var(--white)}
.header .wrap{display:flex;justify-content:space-between;align-items:center;height:94px}
.brand{display:flex;align-items:center;gap:10px}
.brand-dot{width:34px;height:34px;border-radius:50%;background:var(--teal)}
.brand-name{font-family:"Montserrat",sans-serif;font-weight:700;font-size:26px;color:var(--teal);line-height:1}
.brand-tag{font-size:11.5px;color:var(--teal);margin-top:4px}
.header-right{display:flex;flex-direction:column;align-items:flex-end;gap:10px}
.header-row{display:flex;align-items:center;gap:10px}
.call{font-family:"Montserrat",sans-serif;font-weight:600;font-size:14px;color:var(--ink);display:flex;align-items:center;gap:6px}
.call b{color:var(--teal)}
.social{display:flex;gap:5px}
.social i{width:22px;height:22px;border-radius:50%;background:var(--teal);display:block}
.social i:nth-child(3){background:var(--red)}
.cart{background:var(--red);color:#fff;font-size:11px;padding:4px 10px;border-radius:2px;font-weight:600}
.topic-search{width:300px;height:28px;border:1px solid var(--line);border-radius:2px;font-size:11px;color:var(--muted);padding:5px 10px}
/* nav */
.nav{height:46px;background:var(--teal);margin-top:0}
.nav .wrap{display:flex;height:46px}
.nav a{color:#fff;font-family:"Montserrat",sans-serif;font-weight:600;font-size:12.5px;display:flex;align-items:center;padding:0 22px;border-right:1px solid rgba(255,255,255,.25)}
.nav a.active{background:var(--teal-dark)}
/* hero */
.hero{height:384px;position:relative;background:linear-gradient(180deg,#cfe7f1 0%,#b8d59c 55%,#7fae4a 100%)}
.hero .play{position:absolute;left:458px;top:150px}

/* service cards */
.services{height:469px;padding-top:40px}
.cards{display:flex;gap:22px}
.card{width:208px;height:355px;background:#fff;position:relative;box-shadow:0 1px 3px rgba(0,0,0,.12)}
.card h3{height:50px;color:#fff;font-family:"Montserrat",sans-serif;font-size:12.5px;font-weight:600;padding:8px 12px;line-height:1.35}
.card .photo{margin:10px 12px 0;height:110px}
.card p{font-size:11px;color:var(--muted);text-align:center;padding:8px 12px 2px;line-height:1.45}
.card .quiz{display:block;text-align:center;font-size:11px;text-decoration:underline;color:var(--ink)}
.card .btn{position:absolute;left:50%;bottom:-14px;transform:translateX(-50%)}
.c-teal h3{background:var(--teal)}
.c-green h3{background:var(--green)}
.c-dark h3{background:var(--navy)}
.btn{display:inline-block;color:#fff;font-size:11px;font-weight:600;padding:7px 20px;border-radius:14px;background:var(--teal)}
.c-green .btn{background:var(--green)}
.c-dark .btn{background:var(--navy)}
.btn-red{background:var(--red)}

/* main */
.main{height:2805px;background:#fff;padding-top:25px}
.main .wrap{display:flex;justify-content:space-between}
.content{width:590px}
.sidebar{width:285px}
.content h2{font-family:"Montserrat",sans-serif;font-size:17px;font-weight:600;color:var(--ink);margin:18px 0 10px;line-height:1.3}
.content h2:first-child{margin-top:0}
.content p{margin-bottom:10px;color:#4b5356}
.content p a{color:var(--teal);text-decoration:underline}
.ticks{display:grid;grid-template-columns:1fr 1fr;gap:3px 20px;list-style:none;margin:4px 0 14px}
.ticks li{display:flex;align-items:center;gap:7px}
.ticks svg{flex:none}
.ticks a{color:var(--teal)}
.promo{display:flex;gap:20px;margin:14px 0 10px}
.promo figure{width:285px}
.promo .photo{height:130px}
.promo figcaption{height:30px;color:#fff;font-family:"Montserrat",sans-serif;font-size:12.5px;font-weight:600;display:flex;align-items:center;padding:0 12px;gap:8px}
.wide{height:240px;margin:20px 0 22px}
.bullets{list-style:none;margin:6px 0 12px}
.bullets li{display:flex;align-items:center;gap:7px;margin-bottom:3px}
.profile{display:flex;gap:16px;background:#f5f6f6;border:1px solid var(--line);padding:12px;margin-top:22px;height:150px}
.profile .photo{width:150px;height:124px;flex:none}
.profile h4{font-family:"Montserrat",sans-serif;font-size:16px;color:var(--teal);font-weight:600}
.profile small{display:block;font-size:11px;color:var(--muted);margin-bottom:6px}

/* sidebar */
.finder{background:var(--navy);padding:16px;height:275px;color:#fff;border-radius:2px}
.finder h3{font-family:"Montserrat",sans-serif;font-size:14px;font-weight:600;line-height:1.3;margin-bottom:14px}
.finder .field{height:32px;background:#fff;color:var(--muted);font-size:11px;padding:8px 10px;margin-bottom:10px;border-radius:2px;display:flex;justify-content:space-between}
.finder .go{background:var(--teal);text-align:center;font-weight:600;padding:8px;border-radius:2px;margin-top:4px}
.banner{height:175px;margin-top:20px;position:relative;padding:20px;color:#fff}
.banner h4{font-family:"Montserrat",sans-serif;font-size:16px;font-weight:600;line-height:1.3;width:170px;text-shadow:0 1px 2px rgba(0,0,0,.2)}
.banner .btn{position:absolute;right:18px;bottom:18px;border-radius:2px}
.side-head{background:var(--teal);color:#fff;font-family:"Montserrat",sans-serif;font-size:12.5px;font-weight:600;padding:10px 14px;margin-top:22px}
.video{height:200px;position:relative}
.video svg{position:absolute;left:112px;top:70px}
.post{display:flex;gap:12px;height:180px;padding:14px 0;border-bottom:1px solid var(--line)}
.post .photo{width:120px;height:90px;flex:none}
.post time{display:block;font-size:11px;color:var(--teal);font-weight:600}
.post h5{font-size:12px;font-weight:600;color:var(--ink);line-height:1.4;margin:4px 0 6px}
.post .more{font-size:11px;font-weight:700;color:var(--ink)}
.readmore{background:var(--teal);color:#fff;text-align:center;padding:22px 10px;margin-top:14px;height:110px}
.readmore h4{font-family:"Montserrat",sans-serif;font-size:14px;font-weight:600;margin-bottom:12px}
.readmore .btn{border-radius:2px}

/* articles */
.articles{height:320px;padding-top:75px}
.grid3{display:grid;grid-template-columns:repeat(3,1fr);gap:18px 30px}
.article{display:flex;gap:12px;align-items:center;height:95px}
.article .photo{width:140px;height:95px;flex:none}
.article h5{font-family:"Montserrat",sans-serif;font-size:13px;font-weight:600;color:var(--ink);line-height:1.35}
.article .arrow{display:inline-flex;margin-top:8px}

/* login */
.login{height:130px}
.login .box{background:#fff;height:115px;display:flex;align-items:center;gap:20px;padding:0 50px;box-shadow:0 1px 3px rgba(0,0,0,.1)}
.login h3{font-family:"Montserrat",sans-serif;color:var(--teal);font-size:18px;font-weight:600;width:170px}
.login .field{width:260px;height:32px;border:1px solid var(--line);border-radius:16px;font-size:11px;color:var(--muted);padding:7px 14px}
.login .btn{padding:8px 28px}

/* footer */
.footer{height:300px;background:var(--teal);color:#fff;text-align:center;padding-top:100px}
.footer .call{justify-content:center;color:#fff;font-size:15px}
.footer .call b{color:#fff}
.footer .social{justify-content:center;margin:14px 0 22px}
.footer .social i{background:#fff}
.footer .links{font-size:11.5px;text-decoration:underline}
.footer .links span{margin:0 8px}
.footer .copy{font-size:11px;margin-top:22px;opacity:.85}
</style>
</head>
<body>

<div class="topbar">
  <div class="wrap">
    <div><span>Home</span>|<span>About</span>|<span>Resources</span>|<span>Blog</span>|<span>Shop</span></div>
    <div><span>Join Our Associate Program</span>|<span>Marriage Counselling</span>|<span>Relationship Counselling</span></div>
  </div>
</div>

<header class="header">
  <div class="wrap">
    <a class="brand" href="#">
      <span class="brand-dot"></span>
      <span>
        <span class="brand-name">The Luma Haven</span>
        <span class="brand-tag" style="display:block">helping you create loving relationships</span>
      </span>
    </a>
    <div class="header-right">
      <div class="header-row">
        <span class="call">Call Us
          <svg width="16" height="16" viewBox="0 0 24 24"><path fill="#2a8a90" d="M6.6 10.8a15 15 0 006.6 6.6l2.2-2.2a1 1 0 011-.25 11.4 11.4 0 003.6.57 1 1 0 011 1V20a1 1 0 01-1 1A17 17 0 013 4a1 1 0 011-1h3.5a1 1 0 011 1c0 1.25.2 2.45.57 3.57a1 1 0 01-.25 1z"/></svg>
          <b>1300 555 019</b></span>
        <div class="social"><i></i><i></i><i></i><i></i></div>
        <span class="cart">My Cart $ (0.00)</span>
      </div>
      <div class="topic-search">Relationship Information Topics</div>
    </div>
  </div>
</header>

<nav class="nav">
  <div class="wrap">
    <a class="active" href="#">Counselling Types</a>
    <a href="#">Relationship Counselling Locations</a>
    <a href="#">Sex Therapy Locations</a>
    <a href="#">Quizzes</a>
    <a href="#">F.A.Q.'S</a>
    <a href="#">Contact</a>
  </div>
</nav>

<section class="hero" role="img" aria-label="Smiling couple in a sunny field of grass and red flowers, with a counsellor video inset">
  <svg class="play" width="60" height="60" viewBox="0 0 60 60"><circle cx="30" cy="30" r="28" fill="rgba(0,0,0,.25)" stroke="#fff" stroke-width="3"/><path d="M24 18l18 12-18 12z" fill="#fff"/></svg>
</section>

<section class="services">
  <div class="wrap cards">
    <article class="card c-teal">
      <h3>Relationship Counselling</h3>
      <div class="photo" role="img" aria-label="Couple in conversation on a sofa" style="background:linear-gradient(135deg,#c9b7a4,#8d7a6b)"></div>
      <p>Communication, recurring fights, loss of intimacy &amp; trust, power battles...</p>
      <a class="quiz" href="#">Take our Relationship Quiz</a>
      <a class="btn" href="#">Read More</a>
    </article>
    <article class="card c-green">
      <h3>Sex Therapy Counselling</h3>
      <div class="photo" role="img" aria-label="Couple sitting apart on a bed" style="background:linear-gradient(135deg,#d8cfc4,#9c8f83)"></div>
      <p>Low libido, erectile difficulties, premature ejaculation, differing libidos, pain during sex...</p>
      <a class="quiz" href="#">Take our Sex Quiz</a>
      <a class="btn" href="#">Read More</a>
    </article>
    <article class="card c-teal">
      <h3>Anger Management Counselling</h3>
      <div class="photo" role="img" aria-label="Frustrated man holding his head" style="background:linear-gradient(135deg,#b9c3c8,#6f7d84)"></div>
      <p>Managing angry outbursts, expressing your anger in healthy ways...</p>
      <a class="quiz" href="#">Take our Anger Test</a>
      <a class="btn" href="#">Read More</a>
    </article>
    <article class="card c-dark">
      <h3>Narcissism Counselling</h3>
      <div class="photo" role="img" aria-label="Woman looking upset in a dim room" style="background:linear-gradient(135deg,#a99f9a,#5e5450)"></div>
      <p>Managing a relationship with a narcissist, grandiose and lack of empathy...</p>
      <a class="quiz" href="#">Check your Narcissism Profile</a>
      <a class="btn" href="#">Read More</a>
    </article>
  </div>
</section>

<main class="main">
  <div class="wrap">
    <div class="content">
      <h2>We Specialise in Relationship &amp; Marriage Counselling</h2>
      <p>At The Luma Haven, we are a group of psychologists across Australia who are passionate about relationships and helping couples with theirs.</p>
      <p>Our vision is to provide the most highly regarded and comprehensive marriage counselling and relationship counselling, and sex therapy in Australia, at reasonable and affordable rates.</p>
      <p>When we are experiencing relationship and marriage problems, there can be a lot of pain and confusion, and it can often be difficult to cope with the other areas of our lives when we are struggling with problems with our partner.</p>
      <p>We are not taught about relationships and how to have a good one in our schools, so most of us are doing the best we know how, but lack the knowledge on how to create a better relationship.</p>

      <h2>Our Luma Relationship Psychologists</h2>
      <p>Our team of 75 hand chosen Registered Psychologists in 81 locations Australia wide, are skill-fully selected for their knowledge, experience, compassion, and unbiased approach to marriage counselling and sexual therapy.</p>
      <p>In addition all our psychologists take part in our initial Relationship Counselling Methodologies Training and yearly follow-up conferences, ensuring you are in safe and experienced hands.</p>
      <p><a href="#">As we are psychologists, you may be eligible for Government &amp; Private Health Insurance Rebates.</a> We are highly experienced and can help you with all kinds of relationship difficulties.</p>
      <p><b>Here are some of the common ones:</b></p>
      <ul class="ticks">
        <li><svg width="12" height="12" viewBox="0 0 12 12"><rect width="12" height="12" rx="2" fill="#2a8a90"/><path d="M3 6l2 2 4-4" stroke="#fff" stroke-width="1.6" fill="none"/></svg>Affairs</li>
        <li><svg width="12" height="12" viewBox="0 0 12 12"><rect width="12" height="12" rx="2" fill="#2a8a90"/><path d="M3 6l2 2 4-4" stroke="#fff" stroke-width="1.6" fill="none"/></svg>Problems from childhood</li>
        <li><svg width="12" height="12" viewBox="0 0 12 12"><rect width="12" height="12" rx="2" fill="#2a8a90"/><path d="M3 6l2 2 4-4" stroke="#fff" stroke-width="1.6" fill="none"/></svg>Controlling behaviour</li>
        <li><svg width="12" height="12" viewBox="0 0 12 12"><rect width="12" height="12" rx="2" fill="#2a8a90"/><path d="M3 6l2 2 4-4" stroke="#fff" stroke-width="1.6" fill="none"/></svg>Problems with parenting your children</li>
        <li><svg width="12" height="12" viewBox="0 0 12 12"><rect width="12" height="12" rx="2" fill="#2a8a90"/><path d="M3 6l2 2 4-4" stroke="#fff" stroke-width="1.6" fill="none"/></svg>Verbal abuse</li>
        <li><svg width="12" height="12" viewBox="0 0 12 12"><rect width="12" height="12" rx="2" fill="#2a8a90"/><path d="M3 6l2 2 4-4" stroke="#fff" stroke-width="1.6" fill="none"/></svg>Step children and in-laws</li>
        <li><svg width="12" height="12" viewBox="0 0 12 12"><rect width="12" height="12" rx="2" fill="#2a8a90"/><path d="M3 6l2 2 4-4" stroke="#fff" stroke-width="1.6" fill="none"/></svg>Imbalance of power</li>
        <li><svg width="12" height="12" viewBox="0 0 12 12"><rect width="12" height="12" rx="2" fill="#2a8a90"/><path d="M3 6l2 2 4-4" stroke="#fff" stroke-width="1.6" fill="none"/></svg>All forms of family problems</li>
        <li><svg width="12" height="12" viewBox="0 0 12 12"><rect width="12" height="12" rx="2" fill="#2a8a90"/><path d="M3 6l2 2 4-4" stroke="#fff" stroke-width="1.6" fill="none"/></svg>Lack of intimacy</li>
        <li><svg width="12" height="12" viewBox="0 0 12 12"><rect width="12" height="12" rx="2" fill="#2a8a90"/><path d="M3 6l2 2 4-4" stroke="#fff" stroke-width="1.6" fill="none"/></svg>Anger management problems</li>
        <li><svg width="12" height="12" viewBox="0 0 12 12"><rect width="12" height="12" rx="2" fill="#2a8a90"/><path d="M3 6l2 2 4-4" stroke="#fff" stroke-width="1.6" fill="none"/></svg>Poor communication</li>
        <li><svg width="12" height="12" viewBox="0 0 12 12"><rect width="12" height="12" rx="2" fill="#2a8a90"/><path d="M3 6l2 2 4-4" stroke="#fff" stroke-width="1.6" fill="none"/></svg>Porn addiction problems</li>
        <li><svg width="12" height="12" viewBox="0 0 12 12"><rect width="12" height="12" rx="2" fill="#2a8a90"/><path d="M3 6l2 2 4-4" stroke="#fff" stroke-width="1.6" fill="none"/></svg>Jealousy</li>
        <li><svg width="12" height="12" viewBox="0 0 12 12"><rect width="12" height="12" rx="2" fill="#2a8a90"/><path d="M3 6l2 2 4-4" stroke="#fff" stroke-width="1.6" fill="none"/></svg>Pre-marriage programs</li>
        <li><svg width="12" height="12" viewBox="0 0 12 12"><rect width="12" height="12" rx="2" fill="#2a8a90"/><path d="M3 6l2 2 4-4" stroke="#fff" stroke-width="1.6" fill="none"/></svg>Relationship neglect</li>
        <li><svg width="12" height="12" viewBox="0 0 12 12"><rect width="12" height="12" rx="2" fill="#2a8a90"/><path d="M3 6l2 2 4-4" stroke="#fff" stroke-width="1.6" fill="none"/></svg>Affairs</li>
        <li><svg width="12" height="12" viewBox="0 0 12 12"><rect width="12" height="12" rx="2" fill="#2a8a90"/><path d="M3 6l2 2 4-4" stroke="#fff" stroke-width="1.6" fill="none"/></svg>Sexual problems</li>
      </ul>

      <h2>Our Relationship Counselling Approach</h2>
      <p>It is an important part of our policy to take a <a href="#">very positive approach</a> to our relationship counselling.</p>
      <p>We feel it is important to really understand the problems and perspectives of each of you, and at the same time, we find that most couples are looking to find a positive action plan and way through their problems to make changes which have a positive impact and a real sense of hope for their relationship.</p>
      <p>Read more about our approach to counselling in our <a href="#">relationship counselling sessions</a>, and <a href="#">frequently asked questions about the relationship and marriage counselling process.</a></p>
      <div class="promo">
        <figure>
          <div class="photo" role="img" aria-label="Couple reviewing an assessment together" style="background:linear-gradient(135deg,#d9c8b8,#9a8574)"></div>
          <figcaption style="background:var(--teal)">Our Luma Relationship Assessment
            <svg width="10" height="10" viewBox="0 0 10 10"><path d="M3 1l4 4-4 4" stroke="#fff" stroke-width="1.8" fill="none"/></svg></figcaption>
        </figure>
        <figure>
          <div class="photo" role="img" aria-label="Happy couple embracing" style="background:linear-gradient(135deg,#e2cdbf,#a88470)"></div>
          <figcaption style="background:var(--red)">Find out more about us
            <svg width="10" height="10" viewBox="0 0 10 10"><path d="M3 1l4 4-4 4" stroke="#fff" stroke-width="1.8" fill="none"/></svg></figcaption>
        </figure>
      </div>

      <h2>Our Relationship Counselling Locations across Australia</h2>
      <p><b>Here are some of the common ones:</b></p>
      <ul class="ticks">
        <li><svg width="10" height="10" viewBox="0 0 10 10"><path d="M2 1l5 4-5 4" stroke="#2a8a90" stroke-width="2" fill="none"/></svg><a href="#">Sydney</a> – 14 centres</li>
        <li><svg width="10" height="10" viewBox="0 0 10 10"><path d="M2 1l5 4-5 4" stroke="#2a8a90" stroke-width="2" fill="none"/></svg><a href="#">Adelaide</a> – 4 centres</li>
        <li><svg width="10" height="10" viewBox="0 0 10 10"><path d="M2 1l5 4-5 4" stroke="#2a8a90" stroke-width="2" fill="none"/></svg><a href="#">Canberra</a> – 2 centres</li>
        <li><svg width="10" height="10" viewBox="0 0 10 10"><path d="M2 1l5 4-5 4" stroke="#2a8a90" stroke-width="2" fill="none"/></svg><a href="#">Gold Coast</a> – 3 centres</li>
        <li><svg width="10" height="10" viewBox="0 0 10 10"><path d="M2 1l5 4-5 4" stroke="#2a8a90" stroke-width="2" fill="none"/></svg><a href="#">Melbourne</a> – 21 centres</li>
        <li><svg width="10" height="10" viewBox="0 0 10 10"><path d="M2 1l5 4-5 4" stroke="#2a8a90" stroke-width="2" fill="none"/></svg><a href="#">Sunshine Coast</a> – 2 centres</li>
        <li><svg width="10" height="10" viewBox="0 0 10 10"><path d="M2 1l5 4-5 4" stroke="#2a8a90" stroke-width="2" fill="none"/></svg><a href="#">Perth</a> – 12 centres</li>
        <li><svg width="10" height="10" viewBox="0 0 10 10"><path d="M2 1l5 4-5 4" stroke="#2a8a90" stroke-width="2" fill="none"/></svg><a href="#">Cairns</a> – 1 centre</li>
        <li><svg width="10" height="10" viewBox="0 0 10 10"><path d="M2 1l5 4-5 4" stroke="#2a8a90" stroke-width="2" fill="none"/></svg><a href="#">Brisbane</a> – 14 centres</li>
        <li><svg width="10" height="10" viewBox="0 0 10 10"><path d="M2 1l5 4-5 4" stroke="#2a8a90" stroke-width="2" fill="none"/></svg><a href="#">Townsville</a> – 1 centre</li>
        <li><svg width="10" height="10" viewBox="0 0 10 10"><path d="M2 1l5 4-5 4" stroke="#2a8a90" stroke-width="2" fill="none"/></svg><a href="#">Wollongong</a> – 1 centre</li>
        <li><svg width="10" height="10" viewBox="0 0 10 10"><path d="M2 1l5 4-5 4" stroke="#2a8a90" stroke-width="2" fill="none"/></svg><a href="#">Mackay</a> – 1 centre</li>
        <li><svg width="10" height="10" viewBox="0 0 10 10"><path d="M2 1l5 4-5 4" stroke="#2a8a90" stroke-width="2" fill="none"/></svg><a href="#">Central Coast</a> – 2 centres</li>
      </ul>
      <p>Certain clinics also provide after hours and Saturday sessions for your convenience. Click the <a href="#">Locations</a> tab for more information about one of our caring psychologists in your area.</p>

      <div class="photo wide" role="img" aria-label="Young couple smiling among moving boxes in a new home" style="background:linear-gradient(135deg,#e8dccd,#b79a7c)"></div>

      <h2>Communication is a vital skill but not often taught to us</h2>
      <p>Most people feel that their ways of communicating with each other are what hampers us from having a happy healthy relationship.</p>
      <p>Effective interpersonal communication skills are not something that we are usually taught. But for almost everyone who is having difficulties in their relationship, they feel that they are trying to communicate their thoughts and feelings but feel that their partner is not listening.</p>
      <p>Most people then find that they, themselves don't want to listen when they experience their partner as not wanting to listen to them, so the net effect is that neither person gets listened to, and both are frustrated.</p>
      <p>So learning how to communicate your honest thoughts and feelings in a way that your partner more truly takes in is a crucial skill for you to feel that you are in a fulfilling relationship. We can show you some simple but effective principles on how to do this with each other.</p>

      <div class="photo wide" role="img" aria-label="Couple relaxing together on a bed, smiling" style="background:linear-gradient(135deg,#efe4d8,#c2a58b)"></div>

      <h2>We as individuals have specific patterns in our relationships</h2>
      <p>We can also assist you if you want individual help and guidance on your relationship, as you can learn what the patterns in your relationships are showing you about yourself.</p>
      <p>If you have been in a number of relationships and have found yourself repeating the same kind of experiences, which is often the way our relationships play out, we can help you discover the patterns that you might be unwittingly setting up, so you can change these and move into more rewarding relationships in the future.</p>
      <p>Want more information? Please help yourself to our free articles on common relationship problems you may be encountering including:</p>
      <ul class="bullets">
        <li><svg width="10" height="10" viewBox="0 0 10 10"><path d="M2 1l5 4-5 4" stroke="#2a8a90" stroke-width="2" fill="none"/></svg>Why relationships go wrong</li>
        <li><svg width="10" height="10" viewBox="0 0 10 10"><path d="M2 1l5 4-5 4" stroke="#2a8a90" stroke-width="2" fill="none"/></svg>How to recover from an affair</li>
        <li><svg width="10" height="10" viewBox="0 0 10 10"><path d="M2 1l5 4-5 4" stroke="#2a8a90" stroke-width="2" fill="none"/></svg>Move your lost yourself in your relationship</li>
        <li><svg width="10" height="10" viewBox="0 0 10 10"><path d="M2 1l5 4-5 4" stroke="#2a8a90" stroke-width="2" fill="none"/></svg>Improving your relationship</li>
        <li><svg width="10" height="10" viewBox="0 0 10 10"><path d="M2 1l5 4-5 4" stroke="#2a8a90" stroke-width="2" fill="none"/></svg>The secret to more sex</li>
      </ul>
      <p><a href="#">For the latest short, up-to-date articles on relationships, relationship counselling</a>, and relationship co-parenting, please also check out our relationship counselling blog.</p>

      <div class="profile">
        <div class="photo" role="img" aria-label="Portrait of psychologist Maren" style="background:linear-gradient(135deg,#d6c2b0,#8f6e58)"></div>
        <div>
          <h4>Maren</h4>
          <small>Registered Psychologist Brisbane</small>
          <p>B Soc Work, B Ed (Hons), B Ari Sci (Psych), Grad Dip Psych, Grad Dip Couns, M Couns.</p>
          <p>You can read more about <a href="#">relationship counselling</a> here.</p>
        </div>
      </div>
    </div>

    <aside class="sidebar">
      <div class="finder">
        <h3>Find Our Psychologist<br>Near You</h3>
        <div class="field">Type of Counselling <span>▾</span></div>
        <div class="field">Location</div>
        <div class="field">Postcode</div>
        <div class="go">Search</div>
      </div>
      <div class="banner" role="img" aria-label="Stressed woman resting her head in her hands" style="background:linear-gradient(135deg,#5fb6b3,#2a8a90)">
        <h4>Is Anxiety, Depression Or Stress bothering YOU?</h4>
        <span class="btn btn-red">Click Here ▸</span>
      </div>
      <div class="banner" role="img" aria-label="Doctor and health professional in a clinic" style="background:linear-gradient(135deg,#c7d8dd,#7fa5ae)">
        <h4>Information for GPs &amp; Health Professionals</h4>
      </div>
      <div class="side-head">What To Expect From Counselling</div>
      <div class="video" role="img" aria-label="Video of a counselling session with a couple" style="background:linear-gradient(135deg,#cfc1b3,#8b7768)">
        <svg width="60" height="60" viewBox="0 0 60 60"><circle cx="30" cy="30" r="26" fill="rgba(0,0,0,.3)" stroke="#fff" stroke-width="3"/><path d="M25 19l15 11-15 11z" fill="#fff"/></svg>
      </div>
      <div class="side-head">Our Blog ( Relationships &amp; Sex )</div>
      <div class="post"><div class="photo" role="img" aria-label="Couple arguing on a couch" style="background:linear-gradient(135deg,#cbb9a8,#8a7463)"></div><div><time>February 24, 2017</time><h5>What can I do if I'm living with a Narcissist?</h5><a class="more" href="#">Read More ▸</a></div></div>
      <div class="post"><div class="photo" role="img" aria-label="Woman looking away from her partner" style="background:linear-gradient(135deg,#d4c7bd,#958478)"></div><div><time>February 24, 2017</time><h5>Why am I with a Narcissist?</h5><a class="more" href="#">Read More ▸</a></div></div>
      <div class="post"><div class="photo" role="img" aria-label="Tense couple sitting apart" style="background:linear-gradient(135deg,#c0a393,#7d5e4e)"></div><div><time>February 24, 2017</time><h5>How Do I Know If I'm With A Narcissist?</h5><a class="more" href="#">Read More ▸</a></div></div>
      <div class="post"><div class="photo" role="img" aria-label="Man ignoring his partner" style="background:linear-gradient(135deg,#c5bdb6,#837a73)"></div><div><time>February 24, 2017</time><h5>Are You Living With A Stonewaller?</h5><a class="more" href="#">Read More ▸</a></div></div>
      <div class="post"><div class="photo" role="img" aria-label="Partner writing a letter at a desk" style="background:linear-gradient(135deg,#dbd0c3,#a0907f)"></div><div><time>February 10, 2017</time><h5>Letter for a Partner Doubtful About Relationship Counselling</h5><a class="more" href="#">Read More ▸</a></div></div>
      <div class="post"><div class="photo" role="img" aria-label="Couple sitting back to back" style="background:linear-gradient(135deg,#c8c0ba,#7b716a)"></div><div><time>October 19, 2016</time><h5>Do You Wonder Why You and Your Partner Are Together?</h5><a class="more" href="#">Read More ▸</a></div></div>
      <div class="post"><div class="photo" role="img" aria-label="Couple in a heated discussion" style="background:linear-gradient(135deg,#cfbcae,#8c7565)"></div><div><time>October 12, 2016</time><h5>Your Relationship Start on Rocky Ground?</h5><a class="more" href="#">Read More ▸</a></div></div>
      <div class="post"><div class="photo" role="img" aria-label="Couple laughing together outdoors" style="background:linear-gradient(135deg,#e0d3c4,#a88e77)"></div><div><time>October 5, 2016</time><h5>What Are You Like In A Relationship?</h5><a class="more" href="#">Read More ▸</a></div></div>
      <div class="readmore">
        <h4>Would you like to read more?</h4>
        <span class="btn btn-red">Click Here ▸</span>
      </div>
    </aside>
  </div>
</main>

<section class="articles">
  <div class="wrap grid3">
    <a class="article" href="#"><div class="photo" role="img" aria-label="Upset couple after an affair" style="background:linear-gradient(135deg,#c9b4a3,#86705f)"></div><div><h5>How to deal with an affair?</h5><span class="arrow"><svg width="18" height="18" viewBox="0 0 18 18"><rect width="18" height="18" rx="2" fill="#2a8a90"/><path d="M7 5l4 4-4 4" stroke="#fff" stroke-width="1.8" fill="none"/></svg></span></div></a>
    <a class="article" href="#"><div class="photo" role="img" aria-label="Same sex couple holding hands" style="background:linear-gradient(135deg,#d7cabd,#9a877a)"></div><div><h5>Same Sex Relationship &amp; Counselling</h5><span class="arrow"><svg width="18" height="18" viewBox="0 0 18 18"><rect width="18" height="18" rx="2" fill="#2a8a90"/><path d="M7 5l4 4-4 4" stroke="#fff" stroke-width="1.8" fill="none"/></svg></span></div></a>
    <a class="article" href="#"><div class="photo" role="img" aria-label="Woman looking distressed beside partner" style="background:linear-gradient(135deg,#bfb2a8,#776860)"></div><div><h5>Are you living with a narcissist?</h5><span class="arrow"><svg width="18" height="18" viewBox="0 0 18 18"><rect width="18" height="18" rx="2" fill="#2a8a90"/><path d="M7 5l4 4-4 4" stroke="#fff" stroke-width="1.8" fill="none"/></svg></span></div></a>
    <a class="article" href="#"><div class="photo" role="img" aria-label="Couple turned away from each other in bed" style="background:linear-gradient(135deg,#d3c4b8,#937e70)"></div><div><h5>Is one of you an Intimacy Withholder?</h5><span class="arrow"><svg width="18" height="18" viewBox="0 0 18 18"><rect width="18" height="18" rx="2" fill="#2a8a90"/><path d="M7 5l4 4-4 4" stroke="#fff" stroke-width="1.8" fill="none"/></svg></span></div></a>
    <a class="article" href="#"><div class="photo" role="img" aria-label="Partner absorbed in a mobile phone" style="background:linear-gradient(135deg,#c4cbd0,#7f8b93)"></div><div><h5>Is too much phone affecting your relationship?</h5><span class="arrow"><svg width="18" height="18" viewBox="0 0 18 18"><rect width="18" height="18" rx="2" fill="#2a8a90"/><path d="M7 5l4 4-4 4" stroke="#fff" stroke-width="1.8" fill="none"/></svg></span></div></a>
    <a class="article" href="#"><div class="photo" role="img" aria-label="Worried woman with a controlling partner" style="background:linear-gradient(135deg,#cdbdb2,#85736a)"></div><div><h5>Is your relationship safe? Is your partner controlling?</h5><span class="arrow"><svg width="18" height="18" viewBox="0 0 18 18"><rect width="18" height="18" rx="2" fill="#2a8a90"/><path d="M7 5l4 4-4 4" stroke="#fff" stroke-width="1.8" fill="none"/></svg></span></div></a>
  </div>
</section>

<section class="login">
  <div class="wrap box">
    <h3>Members Login</h3>
    <div class="field">Enter Your Email...</div>
    <div class="field">Password</div>
    <span class="btn">Send</span>
  </div>
</section>

<footer class="footer">
  <div class="call">Call Us
    <svg width="16" height="16" viewBox="0 0 24 24"><path fill="#fff" d="M6.6 10.8a15 15 0 006.6 6.6l2.2-2.2a1 1 0 011-.25 11.4 11.4 0 003.6.57 1 1 0 011 1V20a1 1 0 01-1 1A17 17 0 013 4a1 1 0 011-1h3.5a1 1 0 011 1c0 1.25.2 2.45.57 3.57a1 1 0 01-.25 1z"/></svg>
    <b>1300 555 019</b></div>
  <div class="social"><i></i><i></i><i></i></div>
  <div class="links"><span>Privacy Policy</span>|<span>Terms &amp; Conditions</span>|<span>Site Map</span>|<span>Associate Psychologist Program</span>|<span>Contact Us</span></div>
  <div class="copy">© 2017 The Luma Haven. All Rights Reserved</div>
</footer>

</body>
</html>
```